KestrelAV.com

Complete Website Design (Godaddy) and company Branding / Logo Design. The products will sell are only done in-person and are installed. So this site does not need to be an e-commerce site. We will only be giving out information and collecting customer inquires. Website will only need to be about 3 to 5 pages.

```html
<!DOCTYPE html>
<html lang="en">
<head>
<meta charset="utf-8">
<title>KestrelAV – Home</title>
<link rel="stylesheet" href="https://fonts.googleapis.com/css2?family=Poppins:wght@300;400;500;600;700&display=swap">
<style>
  :root {
    --purple: #5b21d6;
    --orange: #ff9500;
    --white: #ffffff;
    --ink: #1a1a1a;
    --field-line: #b9b9c2;
    --footer-rule: rgba(255,255,255,0.35);
  }
  * { margin: 0; padding: 0; box-sizing: border-box; }
  html, body { width: 1200px; height: 738px; overflow: hidden; }
  body { font-family: "Poppins", sans-serif; color: var(--white); }
  .page { position: relative; width: 1200px; height: 738px; overflow: hidden; }
  .hero-photo {
    position: absolute; inset: 0;
    background:
      radial-gradient(ellipse 320px 260px at 360px 230px, #0d0d10 0%, rgba(13,13,16,0.85) 60%, rgba(13,13,16,0) 100%),
      radial-gradient(ellipse 200px 300px at 760px 380px, rgba(40,55,110,0.55) 0%, rgba(40,55,110,0) 100%),
      linear-gradient(180deg, #4b4b4f 0%, #505055 45%, #5a5558 70%, #4a4547 100%);
  }
  .brand {
    position: absolute; left: 76px; top: 50px;
    font-size: 32px; font-weight: 500; letter-spacing: 0.5px;
  }
  .main-nav { position: absolute; top: 57px; left: 611px; display: flex; align-items: center; }
  .main-nav a {
    color: var(--white); text-decoration: none; font-size: 15.5px; font-weight: 400;
    height: 36px; line-height: 36px; letter-spacing: 0.3px;
  }
  .main-nav .current { background: var(--orange); border-radius: 18px; padding: 0 23px; margin-right: 10px; }
  .main-nav a + a { margin-left: 0; }
  .main-nav .gap { margin-left: 42px; }
  .hero-title { position: absolute; left: 74px; top: 212px; line-height: 1; }
  .hero-title .lead { display: block; font-size: 51px; font-weight: 400; letter-spacing: 1px; }
  .hero-title .name { display: block; font-size: 70px; font-weight: 600; margin-top: 4px; letter-spacing: 0.5px; }
  .hero-text {
    position: absolute; left: 75px; top: 358px; width: 620px;
    font-size: 19px; line-height: 30.5px; font-weight: 500; letter-spacing: 0.2px;
  }
  .hero-button {
    position: absolute; left: 75px; top: 501px; width: 179px; height: 52px;
    background: var(--purple); border-radius: 26px; color: var(--white);
    font-size: 20px; font-weight: 700; text-align: center; line-height: 52px; text-decoration: none;
  }
  .quick-contact { position: absolute; left: 780px; top: 150px; width: 380px; height: 500px; }
  .quick-contact svg.card { position: absolute; inset: 0; }
  .quick-title { position: absolute; left: 32px; top: 34px; color: var(--ink); line-height: 1.05; }
  .quick-title .light { display: block; font-size: 32px; font-weight: 400; }
  .quick-title .bold { display: block; font-size: 32px; font-weight: 700; }
  .quick-title-rule { position: absolute; left: 231px; top: 68px; width: 92px; height: 1px; background: #333; }
  .field {
    position: absolute; left: 32px; width: 295px; height: 45px;
    border: 1px solid var(--field-line); border-radius: 23px;
    color: #333; font-size: 13.5px; padding: 0 16px; line-height: 43px; letter-spacing: 0.3px;
  }
  .field.message { height: 99px; border-radius: 26px; line-height: 1; padding-top: 18px; }
  .submit {
    position: absolute; left: 32px; top: 389px; width: 295px; height: 45px;
    background: var(--orange); border-radius: 23px; color: var(--white);
    font-size: 20px; font-weight: 700; text-align: center; line-height: 45px;
  }
  .site-footer { position: absolute; left: 0; top: 682px; width: 1200px; border-top: 1px solid var(--footer-rule); }
  .copyright { position: absolute; left: 75px; top: 20px; font-size: 12.5px; letter-spacing: 0.2px; }
  .social { position: absolute; left: 998px; top: 17px; display: flex; gap: 14px; }
  .social span { width: 22px; height: 22px; border-radius: 50%; background: var(--white); display: block; }
</style>
</head>
<body>
<div class="page">
  <div class="hero-photo" role="img" aria-label="Technician in blue overalls installing a large flat-screen TV on a white media stand, with a toolbox on the floor"></div>

  <div class="brand">KestrelAV</div>

  <nav class="main-nav">
    <a class="current" href="#">Home</a>
    <a href="#">About Us</a>
    <a class="gap" href="#">Services</a>
    <a class="gap" href="#">Products</a>
    <a class="gap" href="#">Contact Us</a>
  </nav>

  <h1 class="hero-title">
    <span class="lead">Welcome to</span>
    <span class="name">KestrelAV</span>
  </h1>

  <p class="hero-text">Duis aute irure dolor in reprehenderit in voluptate velit esse cillum dolore eu fugiat nulla pariatur. Excepteur sint occaecat cupidatat non proident, sunt in culpa qui officia deserunt mollit anim id est laborum.</p>

  <a class="hero-button" href="#">Contact Us</a>

  <form class="quick-contact">
    <svg class="card" width="380" height="500" viewBox="0 0 380 500">
      <polygon points="40,38 356,30 360,478 40,464" fill="#5b21d6" stroke="#5b21d6" stroke-width="24" stroke-linejoin="round"/>
      <polygon points="26,34 334,18 334,456 26,444" fill="#ffffff" stroke="#ffffff" stroke-width="24" stroke-linejoin="round"/>
    </svg>
    <div class="quick-title"><span class="light">Quick</span><span class="bold">Contact Us</span></div>
    <div class="quick-title-rule"></div>
    <div class="field" style="top:119px">Full Name</div>
    <div class="field" style="top:172px">Email Address</div>
    <div class="field" style="top:225px">Phone</div>
    <div class="field message" style="top:279px">Message</div>
    <div class="submit">Submit</div>
  </form>

  <footer class="site-footer">
    <p class="copyright">Copyright © 2024 KestrelAV All Rights Reserved.</p>
    <div class="social" aria-label="Social links">
      <span></span><span></span><span></span><span></span>
    </div>
  </footer>
</div>
</body>
</html>
```